Newspaper Ad Design Project

Hi there,
Our company Brindle Panels is a manufacturer of kitchen and wardrobe doors. We have 2 markets that we sell to 1. Home owners / renovators who would like to put new doors in their kitchen or built in wardrobes and 2. Kitchen and wardrobe companies who buy their doors from us. I need newspaper ads that will appeal to both these markets. The advertisements are for the Sydney local newspapers.
The successful designer will be asked to create several versions of the design for different sized ads.The first ad will be 9 x 13cm wide.
Most important aspects of the design:
1. Must grab attention. When the page is opened, this ad should be the first thing people notice.
2. Clean, simple design, no clutter.
3. Use company logo and colours
I have attached the logo, our brochure and the old ad for wording reference but we can cut out a lot of the text to keep the ad simple and attention grabbing. I want the new ad to look very different. The most important text for the ad is below.
Headline: Renovating your kitchen?
Subheading: Just replace the doors
sub, sub heading: Saving you thousands of $$$
"Get a quote now at www.brindlepanels-example.com.au"
"DIY measure and install"
8631 2975
Please keep the phone number small and website address bigger so that people go to the website instead of just picking up the phone to ask questions.
Target Market(s)
DIY home renovators and owners and Sydney kitchen and wardrobe companies looking to source doors from us.
Industry/Entity Type
It Company

```html
<!DOCTYPE html>
<html lang="en">
<head>
<meta charset="utf-8">
<title>Brindle Panels – Renovating your kitchen?</title>
<link rel="stylesheet" href="https://fonts.googleapis.com/css2?family=Fira+Sans+Condensed:wght@700;800&family=Gochi+Hand&family=Indie+Flower&family=Arimo:wght@400;700&display=swap">
<style>
  :root {
    --brand-yellow: #f7d708;
    --glow: rgba(190, 130, 0, 0.45);
    --ink: #111111;
    --white: #ffffff;
    --black: #000000;
    --photo-light: #e6e4e0;
    --photo-mid: #8a8580;
    --photo-dark: #3a2a22;
  }
  * { margin: 0; padding: 0; box-sizing: border-box; }
  html, body { width: 1200px; height: 831px; overflow: hidden; background: var(--white); }
  .ad {
    position: relative;
    width: 1200px;
    height: 831px;
    background: var(--brand-yellow);
    overflow: hidden;
  }
  .frame { position: absolute; left: 0; top: 0; }
  .headline-group { font-size: inherit; font-weight: inherit; }
  .headline {
    position: absolute;
    display: block;
    left: 0; width: 100%;
    text-align: center;
    white-space: nowrap;
    font-family: "Fira Sans Condensed", "Arial Narrow", sans-serif;
    font-weight: 800;
    font-size: 160px;
    line-height: 1;
    letter-spacing: 0.06em;
    color: var(--white);
    text-shadow: 0 0 22px var(--glow);
  }
  .headline--one { top: 96px; }
  .headline--two { top: 209px; }
  .subheading {
    position: absolute;
    left: 0; width: 100%; top: 353px;
    text-align: center;
    white-space: nowrap;
    font-family: "Fira Sans Condensed", "Arial Narrow", sans-serif;
    font-weight: 700;
    font-size: 106px;
    line-height: 1;
    color: var(--ink);
    text-shadow: 0 0 18px var(--glow);
  }
  .tagline {
    position: absolute;
    left: 0; width: 100%; top: 472px;
    text-align: center;
    white-space: nowrap;
    font-family: "Gochi Hand", cursive;
    font-size: 58px;
    line-height: 1;
    letter-spacing: 0.1em;
    color: var(--ink);
  }
  .footer-band {
    position: absolute;
    left: 0; top: 597px;
    width: 1200px; height: 234px;
    display: flex;
  }
  .kitchen-photo {
    width: 388px; height: 100%;
    background: linear-gradient(180deg, var(--photo-light) 0%, var(--photo-light) 45%, var(--photo-mid) 70%, var(--photo-dark) 100%);
  }
  .contact-panel {
    flex: 1;
    background: var(--black);
    text-align: center;
    color: var(--white);
    padding-top: 34px;
    white-space: nowrap;
  }
  .contact-panel__lead {
    font-family: "Indie Flower", cursive;
    font-size: 62px;
    line-height: 1;
  }
  .contact-panel__web {
    font-family: "Indie Flower", cursive;
    font-size: 48px;
    line-height: 1;
    margin-top: 6px;
    letter-spacing: 0.02em;
  }
  .contact-panel__diy {
    font-family: "Arimo", Arial, sans-serif;
    font-weight: 700;
    font-size: 32px;
    line-height: 1;
    color: var(--brand-yellow);
    margin-top: 20px;
  }
  .contact-panel__phone { font-weight: 400; }
  .brand-mark {
    position: absolute;
    left: 236px; top: 760px;
    display: flex; align-items: center; gap: 8px;
    font-family: "Fira Sans Condensed", "Arial Narrow", sans-serif;
    font-weight: 800;
    font-size: 30px;
    line-height: 1;
    color: var(--white);
  }
  .brand-mark__square {
    width: 20px; height: 20px;
    background: var(--brand-yellow);
  }
</style>
</head>
<body>
  <main class="ad">
    <svg class="frame" width="1200" height="597" viewBox="0 0 1200 597" aria-hidden="true">
      <rect x="18" y="18" width="1164" height="558" fill="none" stroke="#ffffff" stroke-width="2"/>
      <rect x="27" y="27" width="1146" height="540" fill="none" stroke="#ffffff" stroke-width="1.5"/>
    </svg>

    <h1 class="headline-group">
      <span class="headline headline--one">RENOVATING</span>
      <span class="headline headline--two">YOUR KITCHEN?</span>
    </h1>
    <p class="subheading">Just replace the doors</p>
    <p class="tagline">SAVING YOU THOUSANDS OF $$$</p>

    <section class="footer-band">
      <div class="kitchen-photo" role="img" aria-label="Photo of a modern white and dark timber kitchen with dining table and chairs"></div>
      <div class="contact-panel">
        <p class="contact-panel__lead">Get a quote now at</p>
        <p class="contact-panel__web">www.brindlepanels-example.com.au</p>
        <p class="contact-panel__diy">DIY measure and install <span class="contact-panel__phone">- 8631 2975</span></p>
      </div>
    </section>

    <div class="brand-mark">
      <span class="brand-mark__square"></span>
      <span class="brand-mark__name">Brindle Panels</span>
    </div>
  </main>
</body>
</html>
```